Biz Card Design TPVC

New business card for a new company.
Logo was completed by a designer on ArtFlock and looking to continue requesting additional services.
Company Name: Tidal Prime Voltage Collective
Although this company is starting in Canada, we will be moving towards a global presence within the next 6 months.
Key elements to this business are as follows.
Energy Procurement
Energy Reduction Services
Demand Side Consulting
Energy Efficiency Consulting
Saving Clients Money
Helping Them Go "Green"
Managing Their Energy Requirements
Basically the goal for our company is to find the best procurement solution for our clients and reduce their energy consumption. This reduces their expenses and the amount of greenhouse gas they produce on a daily basis.
I have been in the energy footprint for the last 20 years and know that most companies are looking to "do whatever is necessary to get them to sign on the dotted line". I would prefer to walk away from a client that I can't help than to put them into a situation that they will regret for years to come. This is where the "TIDAL" part of the company name comes from.
The following is a catch phrase that encompasses what we do.
"Reducing your carbon footprint & energy bill at the same time!"
The back of the card needs to have this statement along with some sort of illustration. The back is a playground for creative ideas.
The front of the card needs the following.
Logo.
First & Last Name (Gus Marwick)
Title (Energy Warrior)
Phone Number (555) 314-2768
Fax Number (555) 862-4091
Email Address gus@tidalprimevoltage.example
Address 47 Orchard Lane Toronto Ontario K4P 2Z7
I want it to be a card that is remembered when any of my staff give it to a customer. It HAS to stand out.
Target Market(s)
Business Owners, Decision Makers, 30 to 65+
Industry/Entity Type
Business
Look and feel
Each slider illustrates characteristics of the customer's brand and the style your logo design should communicate.

```html
<!DOCTYPE html>
<html lang="en">
<head>
<meta charset="utf-8">
<title>Tidal Prime Voltage Collective — Business Card</title>
<link rel="stylesheet" href="https://fonts.googleapis.com/css2?family=Titillium+Web:wght@400;600;700&family=Saira+Semi+Condensed:wght@500;700&display=swap">
<style>
  :root {
    --page: #e9e6e1;
    --card: #0b0b0b;
    --white: #f4f4f4;
    --grey: #6f6f6f;
    --green: #36c35a;
    --green-deep: #1f8a3c;
    --blue: #3f7fd0;
    --rule: #2f5f9e;
    --shadow: rgba(0, 0, 0, 0.28);
  }
  * { box-sizing: border-box; margin: 0; padding: 0; }
  html, body {
    width: 1200px;
    height: 900px;
    overflow: hidden;
    background: var(--page);
  }
  .stage {
    width: 1200px;
    height: 900px;
    display: flex;
    flex-direction: column;
    align-items: center;
    justify-content: center;
    gap: 50px;
  }
  .card {
    position: relative;
    width: 560px;
    height: 320px;
    background: var(--card);
    box-shadow: 0 10px 28px var(--shadow);
    color: var(--white);
    overflow: hidden;
  }

  /* Back of card */
  .tagline {
    position: absolute;
    left: 34px;
    top: 26px;
    right: 30px;
    font-family: "Saira Semi Condensed", "Arial Narrow", sans-serif;
    font-weight: 700;
    font-size: 27px;
    line-height: 1.12;
    text-transform: uppercase;
    letter-spacing: 0.5px;
  }
  .tagline .mark { color: var(--green); }
  .tagline .carbon { color: var(--grey); }
  .tagline .energy { color: var(--green); }
  .tagline .amp { font-size: 19px; }
  .footprint-art {
    position: absolute;
    left: 34px;
    top: 122px;
    width: 492px;
    height: 120px;
    background: linear-gradient(90deg, #2a2a2a 0%, #1f6e36 45%, var(--green) 100%);
    opacity: 0.85;
    border-radius: 4px;
  }
  .back-name {
    position: absolute;
    right: 30px;
    bottom: 26px;
    font-family: "Titillium Web", sans-serif;
    font-weight: 600;
    font-size: 17px;
    color: var(--blue);
  }

  /* Front of card */
  .brand {
    position: absolute;
    left: 0;
    right: 0;
    top: 58px;
    display: flex;
    align-items: center;
    justify-content: center;
    gap: 12px;
    font-family: "Titillium Web", sans-serif;
    font-weight: 700;
    font-size: 29px;
    color: var(--green);
  }
  .brand-dot {
    width: 26px;
    height: 26px;
    border-radius: 50%;
    background: var(--green-deep);
  }
  .brand-rule {
    position: absolute;
    left: 50px;
    right: 50px;
    top: 116px;
    height: 1px;
    background: var(--rule);
  }
  .contacts {
    position: absolute;
    left: 50px;
    top: 140px;
    font-family: "Titillium Web", sans-serif;
    font-weight: 600;
    font-size: 15px;
    letter-spacing: 0.4px;
  }
  .contact-row {
    display: flex;
    gap: 44px;
    margin-bottom: 12px;
  }
  .contact {
    display: flex;
    align-items: center;
    gap: 10px;
  }
  .contact svg { width: 16px; height: 16px; fill: var(--green); }
  .email { text-transform: uppercase; }
  .address {
    position: absolute;
    left: 30px;
    bottom: 40px;
    font-family: "Saira Semi Condensed", sans-serif;
    font-weight: 500;
    font-size: 12px;
    color: var(--green-deep);
    text-transform: uppercase;
  }
  .person {
    position: absolute;
    right: 30px;
    bottom: 26px;
    text-align: right;
    font-family: "Saira Semi Condensed", sans-serif;
    text-transform: uppercase;
  }
  .person-name {
    font-weight: 700;
    font-size: 22px;
    line-height: 1;
    letter-spacing: 0.5px;
  }
  .person-title {
    font-weight: 500;
    font-size: 10px;
    letter-spacing: 0.6px;
  }
</style>
</head>
<body>
<main class="stage">
  <section class="card card-back" aria-label="Card back">
    <p class="tagline"><span class="mark">"</span>Reducing your <span class="carbon">carbon</span> footprint <span class="amp">&amp;</span><br><span class="energy">energy</span> bill at the same time!<span class="mark">"</span></p>
    <div class="footprint-art" role="img" aria-label="Illustration of footprints fading from grey to green, followed by green dollar signs"></div>
    <p class="back-name">Tidal Prime Voltage Collective</p>
  </section>

  <section class="card card-front" aria-label="Card front">
    <div class="brand"><span class="brand-dot"></span>Tidal Prime Voltage Collective</div>
    <div class="brand-rule"></div>
    <div class="contacts">
      <div class="contact-row">
        <span class="contact">
          <svg viewBox="0 0 16 16" aria-label="Phone"><rect x="4" y="1" width="8" height="14" rx="1.5"/><rect x="5.5" y="3" width="5" height="5" fill="#0b0b0b"/></svg>
          (555) 314-2768
        </span>
        <span class="contact">
          <svg viewBox="0 0 16 16" aria-label="Fax"><rect x="4" y="1" width="8" height="4"/><rect x="1" y="5" width="14" height="7" rx="1"/><rect x="4" y="10" width="8" height="5" fill="#0b0b0b" stroke="#36c35a" stroke-width="1"/></svg>
          (555) 862-4091
        </span>
      </div>
      <div class="contact-row">
        <span class="contact email">
          <svg viewBox="0 0 16 16" aria-label="Email"><rect x="1" y="3" width="14" height="10" rx="1"/><path d="M1.5 3.5 8 9l6.5-5.5" fill="none" stroke="#0b0b0b" stroke-width="1.4"/></svg>
          gus@tidalprimevoltage.example
        </span>
      </div>
    </div>
    <p class="address">47 Orchard Lane Toronto Ontario K4P 2Z7</p>
    <div class="person">
      <p class="person-name">Gus Marwick</p>
      <p class="person-title">Energy Warrior</p>
    </div>
  </section>
</main>
</body>
</html>
```